Letterhead for New Orthopaedic Surgery Practice

My husband and I are starting our own practice named RB Spine & Vitality Center. We would like to create a nice simple but high class letterhead that doesn't use too much solid color ink when printing. I like the colors dark blue, gold, yellow. Open to other suggestions. We will need to list him and I both on the top of the letterhead. Here is the important information:
Lucinda Perrow, M.D. - Hand and Upper Extremity Surgery
Abena Quist, M.D. - Hip & Knee Replacement/General Orthopaedic Surgery
Location: 18735 North Harlow Pkwy
Larkmoor, FL 33480
Phone: 954-218-4650
Fax: 954-582-1346
Email: info@myrbspine.com

The only thing is that the phone and fax numbers will change once we get into our space. I just want to get the design started. I am including several documents which are my previous practice letterhead, my current procedure room letterhead, and our new Logo. The other letterheads are just for examples but please think outside of the box! We would love to see some great designs.

Colors
0054AA
0677BA
7BADD7
CADEEF
E8F1F8
0094D4
00A9DD
6FCCEA
C7EBF8
E9F6FB

Requirements
Must have
• class, elegance, luxury

```html
<!DOCTYPE html>
<html lang="en">
<head>
<meta charset="utf-8">
<title>RB Spine &amp; Vitality Center – Letterhead</title>
<link href="https://fonts.googleapis.com/css2?family=Arimo:wght@400;700&display=swap" rel="stylesheet">
<style>
  :root {
    --navy: #263f8e;
    --cyan: #1eaee0;
    --ink: #555a60;
    --rule: #6a6d72;
    --ghost: #f1f3f8;
    --paper: #ffffff;
    --backdrop: #d9dadc;
  }
  * { box-sizing: border-box; margin: 0; padding: 0; }
  html, body {
    width: 1200px; height: 1159px; overflow: hidden;
    background: var(--backdrop);
    font-family: "Arimo", Arial, sans-serif;
  }
  .letterhead {
    position: absolute; left: 210px; top: 30px;
    width: 780px; height: 1100px;
    background: var(--paper);
    box-shadow: 0 6px 24px rgba(0,0,0,.18);
    overflow: hidden;
  }
  .header {
    position: absolute; left: 56px; right: 56px; top: 48px; height: 96px;
    display: flex; align-items: center;
    border-bottom: 1px solid var(--rule);
    padding-bottom: 12px;
  }
  .brand {
    display: flex; align-items: center; gap: 12px;
    width: 250px;
  }
  .brand-dot {
    width: 14px; height: 14px; border-radius: 50%;
    background: var(--navy); flex: none;
  }
  .brand-name {
    font-weight: 700; font-size: 17px; line-height: 1.2;
    color: var(--navy); letter-spacing: .3px;
  }
  .divider {
    width: 1px; height: 66px; background: var(--rule); flex: none;
  }
  .physicians { padding: 0 22px; width: 250px; }
  .physician + .physician { margin-top: 5px; }
  .physician-name {
    font-weight: 700; font-size: 12.5px; color: var(--cyan);
  }
  .physician-specialty {
    font-size: 10px; line-height: 1.3; color: var(--ink);
  }
  .contact { padding-left: 22px; font-size: 10px; line-height: 1.45; color: var(--ink); }
  .contact-line { display: flex; align-items: center; gap: 5px; }
  .contact-line svg { width: 9px; height: 9px; fill: var(--cyan); flex: none; }
  .address { margin-bottom: 3px; }
  .emblem-ghost {
    position: absolute; left: 90px; top: 330px;
    width: 690px; height: 770px;
    background: radial-gradient(ellipse at 55% 55%, var(--ghost) 0%, var(--ghost) 55%, rgba(241,243,248,0) 75%);
  }
</style>
</head>
<body>
<main class="letterhead">
  <header class="header">
    <div class="brand">
      <span class="brand-dot"></span>
      <span class="brand-name">RB Spine &amp; Vitality Center</span>
    </div>
    <span class="divider"></span>
    <div class="physicians">
      <div class="physician">
        <div class="physician-name">Lucinda Perrow, M.D.</div>
        <div class="physician-specialty">Hand and Upper Extremity Surgery</div>
      </div>
      <div class="physician">
        <div class="physician-name">Abena Quist, M.D.</div>
        <div class="physician-specialty">Hip &amp; Knee Replacement<br>General Orthopaedic Surgery</div>
      </div>
    </div>
    <span class="divider"></span>
    <div class="contact">
      <div class="address">18735 North Harlow Pkwy<br>Larkmoor, FL 33480</div>
      <div class="contact-line">
        <svg viewBox="0 0 10 10" aria-hidden="true"><path d="M1 3c0-1 1-2 4-2s4 1 4 2v1H7V3H3v1H1zM2 5h6l1 4H1z"/></svg>
        954-218-4650
      </div>
      <div class="contact-line">
        <svg viewBox="0 0 10 10" aria-hidden="true"><path d="M3 0h4v3H3zM1 3h8v5H7v2H3V8H1zM4 7h2v2H4z"/></svg>
        954-582-1346
      </div>
      <div class="contact-line">
        <svg viewBox="0 0 10 10" aria-hidden="true"><path d="M0 2h10v6H0zM1 3v.4L5 6l4-2.6V3L5 5.6z"/></svg>
        info@myrbspine.com
      </div>
    </div>
  </header>
  <div class="emblem-ghost" role="img" aria-label="Large faint practice emblem decoration"></div>
</main>
</body>
</html>
```